Business Card for Yachting Management Company

Need a business card design for a new yachting project management company. Attached is the logo for the company.
Our clients are large yacht owners and captains.
Design must be in the style of the logo. Modern, elegant.

Example of data to show:
Peter Hollis
Project Manager
(+34) 612 738 104
peter@quorvane.net
Quorvane Management - Meridel Tower, Office 22 - KRB - Palma de Mallorca

The data above will have to be changed (by me) for the different people in the company over the next years.

Will be printed using PrintNova (Lustre Card Series). They provide these guidelines for the size:
"the actual size of the card is 1050 x 600 pixels. However, the full bleed size is 1083 x 633 pixels, and the safe printing area is 1008 x 558 pixels."

```html
<!DOCTYPE html>
<html lang="en">
<head>
<meta charset="utf-8">
<title>Quorvane Management – Business Card</title>
<link href="https://fonts.googleapis.com/css2?family=Manrope:wght@400;500;700;800&display=swap" rel="stylesheet">
<style>
  :root {
    --backdrop: #d9dde4;
    --card-dark: #121417;
    --card-light: #f4f5f7;
    --ink: #15181d;
    --ink-soft: #2b3038;
    --brand-blue: #6fb2e0;
    --brand-navy: #163a66;
    --rule: #1c2026;
  }
  * { margin: 0; padding: 0; box-sizing: border-box; }
  html, body {
    width: 1200px;
    height: 800px;
    overflow: hidden;
    background: var(--backdrop);
    font-family: "Manrope", sans-serif;
  }
  .canvas {
    width: 1200px;
    height: 800px;
    display: flex;
    flex-direction: column;
    align-items: center;
    justify-content: center;
    gap: 40px;
  }
  .card {
    width: 560px;
    height: 320px;
    position: relative;
    box-shadow: 0 8px 24px rgba(20, 26, 36, 0.18);
  }

  /* Front */
  .card-front {
    background: var(--card-dark);
    display: flex;
    align-items: center;
    justify-content: center;
  }
  .brand-front {
    display: flex;
    align-items: center;
    gap: 14px;
    color: var(--brand-blue);
    font-weight: 700;
    font-size: 34px;
    letter-spacing: 0.02em;
  }
  .brand-front .brand-mark {
    width: 22px;
    height: 22px;
    background: var(--brand-blue);
  }

  /* Back */
  .card-back {
    background: var(--card-light);
    color: var(--ink);
    display: grid;
    grid-template-columns: 150px 1fr;
    grid-template-rows: 1fr auto;
    padding: 34px 30px 34px 34px;
  }
  .person {
    grid-column: 1;
    grid-row: 1;
    align-self: center;
  }
  .person-name {
    font-weight: 800;
    font-size: 19px;
    letter-spacing: -0.01em;
    text-transform: uppercase;
    line-height: 1.1;
  }
  .person-role {
    font-weight: 500;
    font-size: 15px;
    margin-top: 3px;
    padding-bottom: 6px;
    border-bottom: 1.5px solid var(--rule);
    display: inline-block;
  }
  .contact {
    grid-column: 2;
    grid-row: 1;
    align-self: center;
    list-style: none;
    font-size: 12.5px;
    font-weight: 500;
    color: var(--ink-soft);
    padding-left: 26px;
  }
  .contact li {
    display: flex;
    align-items: flex-start;
    gap: 9px;
    margin-bottom: 6px;
    line-height: 1.35;
  }
  .contact svg {
    width: 12px;
    height: 12px;
    flex: none;
    margin-top: 2px;
    fill: var(--ink);
  }
  .brand-back {
    grid-column: 1 / 3;
    grid-row: 2;
    justify-self: end;
    display: flex;
    align-items: center;
    gap: 8px;
    color: var(--brand-navy);
    font-weight: 700;
    font-size: 17px;
  }
  .brand-back .brand-mark {
    width: 11px;
    height: 11px;
    background: var(--brand-navy);
  }
</style>
</head>
<body>
<main class="canvas">

  <section class="card card-front" aria-label="Card front">
    <div class="brand-front">
      <span class="brand-mark"></span>
      <span class="brand-name">Quorvane Management</span>
    </div>
  </section>

  <section class="card card-back" aria-label="Card back">
    <div class="person">
      <p class="person-name">Peter Hollis</p>
      <p class="person-role">Project Manager</p>
    </div>

    <ul class="contact">
      <li>
        <svg viewBox="0 0 24 24" aria-hidden="true"><path d="M6.6 10.8a15.1 15.1 0 0 0 6.6 6.6l2.2-2.2a1 1 0 0 1 1-.25 11.4 11.4 0 0 0 3.6.57 1 1 0 0 1 1 1V20a1 1 0 0 1-1 1A17 17 0 0 1 3 4a1 1 0 0 1 1-1h3.5a1 1 0 0 1 1 1c0 1.25.2 2.45.57 3.6a1 1 0 0 1-.25 1z"/></svg>
        <span>(+34) 612 738 104</span>
      </li>
      <li>
        <svg viewBox="0 0 24 24" aria-hidden="true"><path d="M2 5h20v14H2z M4 7v.5l8 5 8-5V7l-8 5z" fill-rule="evenodd"/></svg>
        <span>peter@quorvane.net</span>
      </li>
      <li>
        <svg viewBox="0 0 24 24" aria-hidden="true"><path d="M12 2a7 7 0 0 0-7 7c0 5.25 7 13 7 13s7-7.75 7-13a7 7 0 0 0-7-7zm0 9.5A2.5 2.5 0 1 1 12 6.5a2.5 2.5 0 0 1 0 5z"/></svg>
        <span>Quorvane Management - Meridel Tower,<br>Office 22 - KRB - Palma de Mallorca</span>
      </li>
    </ul>

    <div class="brand-back">
      <span class="brand-mark"></span>
      <span class="brand-name">Quorvane Management</span>
    </div>
  </section>

</main>
</body>
</html>
```